We need a poster designed for use on facebook, as well as to print out for advertising in local noticeboards and shop windows.
The poster will advertise the Tallowbrook Turf Club 30th Anniversary Ball.
the ball will be held on the 28th April 2018 at the Tallowbrook Community Hall.
Time will be 630pm till late. Ticket Price is $120 which includes 3 course dinner, drinks on arrival and entertainment during the evening.
Additional details will need to be added to the poster at a later date.
The tallowbrook Turf Club is a horse racing club run by the community. The club has been incorporateds for 30 years. This Ball will be a celebration of that anniversary.

Target Market(s)

Middlemount Community

Industry/Entity Type

Club

Font styles to use
Serif
Decorative

Colors
1b1b1b
fbfbfb
6b449b
886aae
a64599
ffc214

Requirements
Must have
• Include
• where when time and cost
• ticket inclusions
• entertainement by Colin Verity
Nice to have
• Attached are some images for inspiration.
• It would be nice to have the race club logo included somewhere however not prominant.
Should not have
• Abstract geometriic lines
• images of people
• primary colours

```html
<!DOCTYPE html>
<html lang="en">
<head>
<meta charset="utf-8">
<title>Tallowbrook Turf Club 30th Anniversary Ball</title>
<link rel="stylesheet" href="https://fonts.googleapis.com/css2?family=Cinzel+Decorative:wght@700;900&family=Playfair+Display:ital,wght@0,400;0,600;0,700;0,800;1,400&display=swap">
<style>
  :root {
    --page: #e9e9e9;
    --ink-dark: #1b1b1b;
    --white: #fbfbfb;
    --purple: #6b449b;
    --lavender: #886aae;
    --magenta: #a64599;
    --gold: #ffc214;
    --plum-deep: #2a1838;
    --disc-dark: #2b1a47;
  }
  * { box-sizing: border-box; margin: 0; padding: 0; }
  html, body { width: 1200px; height: 2556px; overflow: hidden; background: var(--page); }
  body { position: relative; font-family: "Playfair Display", Georgia, serif; color: var(--white); }

  .poster {
    position: absolute; left: 60px; top: 503px;
    width: 1080px; height: 1550px; overflow: hidden;
    background: var(--plum-deep);
    box-shadow: 0 10px 30px rgba(0,0,0,.25);
  }
  .poster-art { position: absolute; inset: 0; width: 1080px; height: 1550px; }

  .club-mark { position: absolute; left: 38px; top: 80px; width: 200px; display: flex; flex-direction: column; align-items: center; gap: 10px; }
  .club-mark-dot { width: 70px; height: 70px; border-radius: 50%; background: var(--gold); }
  .club-mark-name { font-weight: 700; font-size: 26px; line-height: 1.15; text-align: center; color: var(--white); }

  .club-banner {
    position: absolute; left: 271px; top: 92px; width: 645px; height: 70px;
    background: var(--ink-dark); display: flex; align-items: center; justify-content: center;
    font-family: "Cinzel Decorative", Georgia, serif; font-weight: 700; font-size: 30px; letter-spacing: .5px; color: var(--white);
  }

  .event-title {
    position: absolute; left: 180px; top: 462px; width: 760px; text-align: center; white-space: nowrap;
    font-family: "Cinzel Decorative", Georgia, serif; font-weight: 900; line-height: 1;
    text-shadow: 2px 2px 3px rgba(0,0,0,.6);
  }
  .event-title .num { font-size: 72px; }
  .event-title sup { font-size: 38px; vertical-align: 30px; margin-right: 4px; }
  .event-title .word { font-size: 56px; }
  .event-ball {
    position: absolute; right: 210px; top: 548px;
    font-family: "Cinzel Decorative", Georgia, serif; font-size: 50px; font-weight: 900;
    text-shadow: 2px 2px 3px rgba(0,0,0,.6);
  }

  .event-month {
    position: absolute; left: 250px; top: 628px; width: 52px; height: 138px; background: var(--gold);
    display: flex; align-items: center; justify-content: center;
  }
  .event-month span { transform: rotate(-90deg); font-weight: 700; font-size: 34px; white-space: nowrap; color: var(--ink-dark); }
  .event-day { position: absolute; left: 314px; top: 596px; font-size: 160px; font-weight: 800; line-height: 1; }
  .event-at { position: absolute; left: 690px; top: 706px; font-size: 42px; font-weight: 400; font-style: italic; }

  .event-venue { position: absolute; left: 180px; top: 780px; width: 760px; text-align: center; font-weight: 700; font-size: 50px; line-height: 60px; }
  .event-time { position: absolute; left: 180px; top: 906px; width: 760px; text-align: center; font-size: 46px; line-height: 1; }
  .event-time b { font-weight: 700; }
  .event-time small { font-size: 30px; font-weight: 700; }

  .ticket-tag {
    position: absolute; left: 671px; top: 1099px; width: 292px; height: 62px; background: var(--gold); border-radius: 14px;
    display: flex; align-items: center; justify-content: center; font-weight: 700; font-size: 36px; color: var(--ink-dark);
  }
  .ticket-price { position: absolute; left: 668px; top: 1166px; font-weight: 800; font-size: 120px; line-height: 1; }
  .ticket-includes { position: absolute; left: 672px; top: 1306px; width: 390px; font-size: 22px; line-height: 32px; font-weight: 400; }
  .ticket-includes b { font-weight: 700; }

  .performer-photo { position: absolute; left: 31px; top: 1303px; width: 320px; height: 228px; background: linear-gradient(135deg, #6e4a3c 0%, #a57c66 45%, #d5c2b4 75%, #e8e4e0 100%); }
  .performer-label { position: absolute; left: 364px; top: 1384px; font-size: 22px; font-weight: 700; }
  .performer-name { position: absolute; left: 364px; top: 1418px; font-size: 36px; font-weight: 400; font-style: italic; }
  .performer-rule { position: absolute; left: 364px; top: 1492px; width: 290px; height: 2px; background: var(--white); }
  .web-address { position: absolute; left: 690px; top: 1474px; font-size: 32px; font-weight: 400; }
  .web-address span { color: var(--gold); font-weight: 700; }
</style>
</head>
<body>
  <main class="poster">
    <svg class="poster-art" viewBox="0 0 1080 1550" aria-hidden="true">
      <defs>
        <radialGradient id="glow-top" cx="540" cy="60" r="620" gradientUnits="userSpaceOnUse">
          <stop offset="0" stop-color="#ffc214"/><stop offset=".5" stop-color="#8a6a1a"/><stop offset="1" stop-color="#2a1838" stop-opacity="0"/>
        </radialGradient>
        <radialGradient id="glow-left" cx="120" cy="620" r="520" gradientUnits="userSpaceOnUse">
          <stop offset="0" stop-color="#e0a030"/><stop offset=".55" stop-color="#a64599" stop-opacity=".7"/><stop offset="1" stop-color="#a64599" stop-opacity="0"/>
        </radialGradient>
        <radialGradient id="glow-bottom" cx="520" cy="1060" r="620" gradientUnits="userSpaceOnUse">
          <stop offset="0" stop-color="#d9a0d0"/><stop offset=".4" stop-color="#a64599"/><stop offset="1" stop-color="#6b449b" stop-opacity="0"/>
        </radialGradient>
        <radialGradient id="glow-right" cx="1000" cy="640" r="380" gradientUnits="userSpaceOnUse">
          <stop offset="0" stop-color="#886aae" stop-opacity=".85"/><stop offset="1" stop-color="#886aae" stop-opacity="0"/>
        </radialGradient>
        <radialGradient id="disc" cx="560" cy="640" r="420" gradientUnits="userSpaceOnUse">
          <stop offset="0" stop-color="#4a2f72"/><stop offset="1" stop-color="#2b1a47"/>
        </radialGradient>
        <filter id="blur" x="-20%" y="-20%" width="140%" height="140%"><feGaussianBlur stdDeviation="14"/></filter>
      </defs>
      <rect width="1080" height="1550" fill="#2a1838"/>
      <rect width="1080" height="1550" fill="url(#glow-top)"/>
      <rect width="1080" height="1550" fill="url(#glow-left)"/>
      <rect width="1080" height="1550" fill="url(#glow-right)"/>
      <rect width="1080" height="1550" fill="url(#glow-bottom)"/>
      <rect x="0" y="1250" width="1080" height="300" fill="#1b1b1b" opacity=".35"/>

      <circle cx="560" cy="676" r="440" fill="#886aae" opacity=".7" filter="url(#blur)"/>
      <circle cx="560" cy="676" r="425" fill="#a64599"/>
      <circle cx="560" cy="676" r="425" fill="none" stroke="#ffc214" stroke-width="8" opacity=".85"/>
      <circle cx="560" cy="676" r="392" fill="url(#disc)"/>
    </svg>

    <div class="club-mark">
      <span class="club-mark-dot"></span>
      <span class="club-mark-name">Tallowbrook<br>Turf Club</span>
    </div>
    <div class="club-banner">TALLOWBROOK TURF CLUBS</div>

    <h1 class="event-title"><span class="num">30</span><sup>th</sup><span class="word">ANNIVERSARY</span></h1>
    <div class="event-ball">BALL</div>
    <div class="event-month"><span>April</span></div>
    <div class="event-day">28th</div>
    <div class="event-at">at the</div>
    <div class="event-venue">TALLOWBROOK<br>COMMUNITY HALL</div>
    <div class="event-time"><b>6.30</b><small>pm</small> ONWARDS</div>

    <div class="ticket-tag">TICKETS @</div>
    <div class="ticket-price">$120</div>
    <p class="ticket-includes">Which Includes 3 Course <b>Dinner</b>, <b>Drinks On Arrival</b> And <b>Entertainment During the</b> Evening</p>

    <div class="performer-photo" role="img" aria-label="Photo of performer Colin Verity"></div>
    <div class="performer-label">Performance By</div>
    <div class="performer-name">Colin Verity</div>
    <div class="performer-rule"></div>
    <div class="web-address">www.<span>tbturfclub</span>.com</div>
  </main>
</body>
</html>
```